We have 'joined together' 6 micro-sites with a common theme. Looking to upgrade the design of a total of 26 pages on the abovementioned sites, whilst maintaining a common look and feel.

Goal is to improve customer experience and conversion rate, whilst maintaining Vantro rankings. New design to be responsive to different devices and SEO optimised

We prefer simple designs with the cleaness of Zelqo.com, however with more descriptive text. Target audience are business managers and owners, so site should convey professional capability, with a hint of playfulness. After all data can be fun? No?

See attached doc for further details.

Update: 19/8/2014. Following further consideration, the HTML coding no longer required. Once design is finalised, we require a PSD file for each page showing the full page layout, including all images and icons. We will extract the relevant bits from the PSD and do the coding and css inhouse.
Updates

Hi All The Pelquin Collective - PSD Design Only. HTML no longer required Following further consideration, the HTML / Css coding aspect of the project NO longer required. Once design is finalised, we require a PSD file from you for each of the 26 web pages, showing the page layout and including all images and icons. If one page layout is the same as another, then we request that you just supply images and icons for that page in a PSD file. We will then extract the relevant bits from the PSD and we will do the coding and css inhouse. Our main aim is to get an awesome, blow-your-sox-off design that compels users to convert. Many thanks in anticipation Oliver.

Project Deadline Extended
Reason: Changed deliverables from PSD, HTML and Coding t o PSD only. Hopefully this change will allow previous designers who were not interested to reconsider. Many thanks Oliver

Target Market(s)

Target market is business & IT managers within Australian organisations who are having problems with their data. Site must convey the impression that we are:
1) Very capable
2) Professional in our dealings
3) Reliable & trustworthy
4) Just a little bit quirky

Aprox. 60% of users are female, 40% male. Typically in the 30 to 55 year old bracket.

Number 1 requirements is that we don't embarrass our clients in any way.
2nd is that we do a good high quality job, delivering a good result.

We are not the cheapest nor the most expensive data shop around. We offer good value-for-money solutions. We are also reliable, friendly and available

Industry/Entity Type

Business

Font styles to use
Sans Serif

Requirements
Must have
• Simple yet information dense design. The "who we are" and "what we do" to be immediately visible above the fold. Images to be high quality. Good usability.
Simple navigation structure. Easy for users to find the info that they want.

In summary a simple, but good looking site, that compels users to contact us
Should not have
• No flash, fancy automation, rotating images, pop-ups etc.

```html
<!DOCTYPE html>
<html lang="en">
<head>
<meta charset="utf-8">
<title>The Pelquin Collective</title>
<link href="https://fonts.googleapis.com/css2?family=Arimo:wght@400;700&display=swap" rel="stylesheet">
<style>
:root{
  --orange:#f26a10;
  --dark:#3b3b3b;
  --darker:#262626;
  --nav:#4a4a4a;
  --text:#333;
  --muted:#555;
  --band:#eeeeee;
  --footer-text:#e6e6e6;
  --rule:#dcdcdc;
}
*{margin:0;padding:0;box-sizing:border-box}
html,body{width:842px;height:1200px;overflow:hidden}
body{position:relative;background:#fff;font-family:"Arimo",Arial,sans-serif;color:var(--text)}
.abs{position:absolute}

.site-header{left:0;top:0;width:842px;height:62px;background:var(--dark)}
.brand{left:124px;top:15px;font-size:25px;font-weight:700;color:#fff;letter-spacing:.2px}
.call{left:602px;top:17px;color:#fff;display:flex;align-items:center;gap:6px}
.call small{display:block;font-size:9.5px}
.call strong{display:block;font-size:13.5px;font-weight:400}

.main-nav{left:0;top:62px;width:842px;height:26px;background:var(--nav);border-top:1px solid #777;border-bottom:1px solid #777}
.main-nav ul{list-style:none;display:flex;position:absolute;left:123px;top:0;height:24px}
.main-nav li{font-size:8.8px;color:#fff;line-height:24px;padding:0 10px}
.main-nav li.active{background:var(--orange);padding:0 12px;font-weight:700}

.hero{left:0;top:88px;width:842px;height:216px;background:var(--dark)}
.hero-photo{left:118px;top:0;width:600px;height:216px;background:linear-gradient(120deg,#d9dee3 0%,#b6c3d0 40%,#8d9aab 70%,#cfd5db 100%)}
.hero-caption{left:118px;top:178px;width:600px;height:38px;background:rgba(40,40,40,.55);color:#fff;font-size:15px;line-height:19px;padding:0 2px}
.dots{display:flex;gap:3px}
.dots i{width:5px;height:5px;border-radius:50%;background:#fff}
.dots i:first-child{background:var(--orange)}

.section-title{font-size:16.5px;font-weight:700;color:var(--orange);letter-spacing:.2px}
.rule{border-bottom:1px dashed var(--rule)}

.services{left:124px;top:368px;width:598px;display:flex;justify-content:space-between}
.service{text-align:center;font-size:9.8px;color:var(--text);width:90px}
.service svg{display:block;margin:0 auto 5px;height:40px}
.service.active{color:var(--orange);font-weight:700}

.body-copy{font-size:8.4px;line-height:12px;color:var(--text);text-align:justify}
.callout{left:123px;top:574px;width:392px;height:56px;border:1px solid #ccc;border-radius:5px;padding:8px 7px;font-size:8.4px;line-height:12px;box-shadow:0 8px 8px -6px rgba(0,0,0,.25)}
.callout .tel{color:var(--orange);font-weight:700;font-size:9.4px}

.resources{left:526px;top:449px;width:193px;height:185px;border:3px solid var(--orange);background:#fff;overflow:hidden}
.resources-photo{left:0;top:0;width:110px;height:179px;background:linear-gradient(160deg,#f3f3f3,#d9c9b8 55%,#2e3a44)}
.resources-head{right:6px;top:8px;text-align:right;font-weight:700;line-height:21px}
.resources-head .r{color:#d3202a;font-size:23px}
.resources-head .d{color:#222;font-size:19px}
.resources-head .s{color:#d3202a;font-size:15.5px}
.tags{right:5px;top:107px;display:flex;flex-direction:column;align-items:flex-end;gap:2px}
.tags span{background:var(--orange);color:#fff;font-size:8px;font-weight:700;padding:1px 3px;line-height:10px}

.benefit h3{font-size:10px;font-weight:700;display:flex;align-items:center;gap:5px;margin-bottom:2px}
.benefit p{font-size:8.3px;line-height:12px}

.quotes{left:526px;top:697px;width:190px}
.quote{font-size:8.3px;line-height:12.3px;margin-bottom:27px}
.quote .mark{color:#bbb;font-size:13px;font-weight:700;vertical-align:-3px}
.quote .who{text-align:right;font-size:7.8px;line-height:10px;margin-top:5px;color:var(--muted);padding-right:14px}
.quote .who b{font-weight:700}

.clients{left:0;top:940px;width:842px;height:73px;background:var(--band)}
.clients-label{left:124px;top:23px;color:var(--orange);font-size:10.5px;font-weight:700;font-style:italic;line-height:13px}
.client{top:26px;display:flex;align-items:center;gap:5px;font-size:15px;font-weight:700}
.client i{display:inline-block;width:12px;height:12px}

.site-footer{left:0;top:1013px;width:842px;height:159px;background:var(--dark)}
.foot-col{top:28px;list-style:none;font-size:8.8px;color:var(--footer-text);line-height:16.6px}
.foot-div{top:24px;width:1px;height:116px;background:#555}
.foot-brand{left:606px;top:30px;width:128px;text-align:center;color:#8e8e8e;font-size:20px;line-height:24px}
.foot-abn{left:606px;top:101px;width:128px;text-align:center;color:var(--footer-text);font-size:8px}
.copyright{left:0;top:1172px;width:842px;height:28px;background:var(--darker);color:#ddd;font-size:8px;text-align:center;line-height:28px}
</style>
</head>
<body>

<header class="site-header abs">
  <div class="brand abs">The Pelquin Collective</div>
  <div class="call abs">
    <svg width="20" height="20" viewBox="0 0 20 20"><circle cx="10" cy="10" r="9" fill="none" stroke="#fff" stroke-width="1.3"/><path d="M7 5.5c-1 1-1 3 1 6s4 4 5.5 3l.8-1-2-1.5-1 .8c-1-.4-2.4-2-2.8-3l.8-1L8.5 4.7z" fill="#fff"/></svg>
    <div><small>Call Us Today</small><strong>1300 555 019</strong></div>
  </div>
</header>

<nav class="main-nav abs">
  <ul>
    <li class="active">HOME</li><li>DATA ANALYSIS</li><li>DATA CLEANSING</li><li>DATA MINING</li><li>DATA SCRAPING</li><li>DATA WAREHOUSE</li><li>BLOG</li><li>CONTACT</li>
  </ul>
</nav>

<section class="hero abs">
  <div class="hero-photo abs" role="img" aria-label="Photograph of a business team reviewing reports around a laptop"></div>
  <div class="hero-caption abs">Our Data Mining Services Utilise Advanced Statistical, Numerical And Multivariate Techniques To Identify Areas Of Opportunity Within Your Organisation’s Data.</div>
  <div class="dots abs" style="left:690px;top:205px"><i></i><i></i><i></i><i></i></div>
</section>

<h2 class="section-title abs" style="left:126px;top:321px">WHAT WE DO</h2>
<div class="rule abs" style="left:126px;top:344px;width:594px"></div>

<div class="services abs">
  <div class="service active">
    <svg viewBox="0 0 40 40" width="40"><g fill="#f26a10"><rect x="3" y="26" width="4" height="10"/><rect x="9" y="22" width="4" height="14"/><rect x="15" y="24" width="4" height="12"/><rect x="21" y="18" width="4" height="18"/><rect x="27" y="14" width="4" height="22"/><rect x="33" y="16" width="4" height="20"/></g><polyline points="4,20 11,14 17,17 24,10 30,7 36,4" fill="none" stroke="#f26a10" stroke-width="2"/><circle cx="36" cy="4" r="2" fill="#f26a10"/></svg>
    Data Analysis</div>
  <div class="service">
    <svg viewBox="0 0 40 40" width="40"><path d="M34 3 22 20" stroke="#444" stroke-width="3"/><path d="M16 18l9 6c-2 8-9 12-16 11 3-2 4-4 4-6-2 1-4 1-6 0 4-2 6-6 9-11z" fill="#444"/><circle cx="6" cy="10" r="1.6" fill="#444"/><circle cx="10" cy="6" r="1.2" fill="#444"/><circle cx="4" cy="18" r="1.2" fill="#444"/></svg>
    Data Cleansing</div>
  <div class="service">
    <svg viewBox="0 0 40 40" width="40"><circle cx="16" cy="16" r="11" fill="none" stroke="#444" stroke-width="3"/><path d="M16 10v12M10 16h12" stroke="#444" stroke-width="2.5"/><path d="M24 24l11 11" stroke="#444" stroke-width="5" stroke-linecap="round"/></svg>
    Data Mining</div>
  <div class="service">
    <svg viewBox="0 0 40 40" width="40"><rect x="3" y="4" width="34" height="24" rx="2" fill="#444"/><rect x="6" y="7" width="28" height="18" fill="#fff"/><circle cx="20" cy="16" r="3.5" fill="#444"/><path d="M14 31h12l2 4H12z" fill="#444"/></svg>
    Data Scraping</div>
  <div class="service">
    <svg viewBox="0 0 40 40" width="40"><g fill="#444"><ellipse cx="20" cy="8" rx="14" ry="5"/><path d="M6 12c0 3 6 5 14 5s14-2 14-5v6c0 3-6 5-14 5s-14-2-14-5z"/><path d="M6 22c0 3 6 5 14 5s14-2 14-5v6c0 3-6 5-14 5s-14-2-14-5z"/></g></svg>
    Data Warehouse</div>
  <div class="service">
    <svg viewBox="0 0 40 40" width="40"><g fill="#fff" stroke="#444" stroke-width="2.5"><rect x="18" y="3" width="16" height="22" rx="2"/><rect x="12" y="8" width="16" height="22" rx="2"/><rect x="6" y="13" width="16" height="24" rx="2"/></g></svg>
    Data Resources</div>
</div>

<h2 class="section-title abs" style="left:124px;top:447px">WHO WE ARE</h2>
<div class="rule abs" style="left:124px;top:469px;width:388px"></div>
<p class="body-copy abs" style="left:124px;top:479px;width:389px">The Pelquin Collective is a Melbourne based business offering a comprehensive range of data services. We specialise in data analysis, data cleansing, data mining, data scraping and data warehouses.</p>
<p class="body-copy abs" style="left:124px;top:513px;width:389px">Our goal is to help you extract value from your data in the form of pragmatic insights, trends and relationships. And then to analyse, interpret and use these findings in innovative ways that empower you to manage your organisation for greater profit, with improved decision-making and enhanced strategic, tactical and operational insight.</p>
<div class="callout abs">If you have <b>data and a question</b>, <b>challenge or opportunity,</b> we can help. We’ve been around since 2005 and worked on a diverse range of projects.<br>Call us for a friendly discussion on <span class="tel">1300 555 019</span></div>

<aside class="resources abs">
  <div class="resources-photo abs" role="img" aria-label="Photograph of a smiling businesswoman"></div>
  <div class="resources-head abs"><div class="r">CHECK</div><div class="d">OUT OUR</div><div class="s">RESOURCES</div></div>
  <div class="tags abs"><span>DATA MINING</span><span>DATA ANALYSIS</span><span>DATA SCRAPING</span><span>DATA CLEANSING</span><span>DATA WAREHOUSE</span></div>
</aside>

<h2 class="section-title abs" style="left:124px;top:661px">YOUR BENEFITS</h2>
<div class="rule abs" style="left:124px;top:684px;width:388px"></div>
<p class="body-copy abs" style="left:124px;top:695px;width:378px;text-align:left">Our core speciality is solving business problems that require complex data analysis, cleansing, mining or modelling techniques. Your benefits include:</p>

<div class="benefit abs" style="left:124px;top:722px;width:385px">
  <h3><svg width="10" height="10" viewBox="0 0 10 10"><rect x=".6" y=".6" width="8.8" height="8.8" fill="none" stroke="#333" stroke-width="1.2"/><path d="M2 5l2 2 5-6" fill="none" stroke="#333" stroke-width="1.6"/></svg>Fast ROI</h3>
  <p>Quick access to skilled data professionals, without the overhead of building and maintaining your own infrastructure and team. Our fees are typically small in contrast to the additional profits or savings that our projects generate for our clients.</p>
</div>
<div class="benefit abs" style="left:124px;top:783px;width:385px">
  <h3><svg width="10" height="10" viewBox="0 0 10 10"><rect x=".6" y=".6" width="8.8" height="8.8" fill="none" stroke="#333" stroke-width="1.2"/><path d="M2 5l2 2 5-6" fill="none" stroke="#333" stroke-width="1.6"/></svg>Innovative Practical Solutions</h3>
  <p>We find smart ways to extract useful information from incomplete and disorganised data. We also have extensive industry experience AND the quantitative rigour to generate innovative yet pragmatic value-adding solutions.</p>
</div>
<div class="benefit abs" style="left:124px;top:844px;width:385px">
  <h3><svg width="10" height="10" viewBox="0 0 10 10"><rect x=".6" y=".6" width="8.8" height="8.8" fill="none" stroke="#333" stroke-width="1.2"/><path d="M2 5l2 2 5-6" fill="none" stroke="#333" stroke-width="1.6"/></svg>Connected To Major Universities</h3>
  <p>We have relationships with leading practitioners at major universities and business schools within Australia. This provides us with ready access to extensive expertise and the latest developments. We have never turned down a project due to it being too complex.</p>
</div>
<div class="benefit abs" style="left:124px;top:905px;width:385px">
  <h3><svg width="10" height="10" viewBox="0 0 10 10"><rect x=".6" y=".6" width="8.8" height="8.8" fill="none" stroke="#333" stroke-width="1.2"/><path d="M2 5l2 2 5-6" fill="none" stroke="#333" stroke-width="1.6"/></svg>Always Confidential And Discreet</h3>
</div>

<h2 class="abs" style="left:528px;top:658px;font-size:10.5px;font-weight:700;color:var(--orange)">WHAT OTHERS ARE SAYING</h2>
<div class="rule abs" style="left:526px;top:684px;width:197px"></div>
<div class="quotes abs">
  <div class="quote"><span class="mark">“</span> I like the way that you can quantify benefits.
    <div class="who">- MARTIN R<br><b>Chief Executive Officer</b></div></div>
  <div class="quote" style="margin-top:4px"><span class="mark">“</span> Thanks for your work with our data, it certainly looks and feels clean.
    <div class="who">- HELENA T<br><b>Marketing Officer</b></div></div>
  <div class="quote" style="margin-top:4px"><span class="mark">“</span> Thanks for the fast turnaround on our de-duplication project. ...I’m so impressed that I have already recommended you to two of our suppliers.
    <div class="who" style="margin-top:2px">- SAM W<br><b>Marketing Manager</b></div></div>
</div>

<section class="clients abs">
  <div class="clients-label abs">SOME PEOPLE<br>WE WORK WITH</div>
  <div class="client abs" style="left:238px;color:#8a1c2b"><i style="border-radius:50%;background:#b3202f"></i>Korvane Pharma</div>
  <div class="client abs" style="left:414px;color:#1f3f7a"><i style="border-radius:50%;background:#e0a21b"></i>Ristelo</div>
  <div class="client abs" style="left:528px;color:#f26a10"><i style="border-radius:50%;background:#f26a10"></i>Mabrix</div>
  <div class="client abs" style="left:650px;color:#222"><i style="background:#d3202a"></i>Halden Care</div>
</section>

<footer class="site-footer abs">
  <ul class="foot-col abs" style="left:119px"><li>Home</li><li>Algorithm Creation</li><li>Cleansing Nimbly CRM Data</li><li>Customer Analysis</li><li>Data Analysis Methods</li><li>Data Checking</li><li>Data Cleansing</li></ul>
  <div class="foot-div abs" style="left:258px"></div>
  <ul class="foot-col abs" style="left:273px"><li>Data Deduplication</li><li>Data Management</li><li>Data Merging</li><li>Data Migration</li><li>Data Mining</li><li>Data Scraping</li><li>Data Verification</li></ul>
  <div class="foot-div abs" style="left:360px"></div>
  <ul class="foot-col abs" style="left:375px"><li>Data Warehouse</li><li>Data Warehouse Methodology</li><li>Financial Analysis</li><li>Procurement Analysis</li><li>Quarix Report Writing</li><li>Text Analysis</li><li>Data Analysis</li></ul>
  <div class="foot-div abs" style="left:507px"></div>
  <ul class="foot-col abs" style="left:521px"><li>Comments Policy</li><li>Contact Us</li><li>Disclaimer</li><li>Blog</li><li>Privacy Statement</li><li>Login</li></ul>
  <div class="foot-div abs" style="left:605px"></div>
  <div class="foot-brand abs">The Pelquin<br>Collective</div>
  <div class="foot-abn abs">ABN: 41 607 228 391</div>
</footer>
<div class="copyright abs">Copyright ©2014, The Pelquin Collective is a division of Brightfield Holdings (Australia) Pty Ltd.</div>

</body>
</html>
```